Powerpoint Template Design

We need a Corporate Powerpoint Template. We are a small boutique IT consultancy specialized in Business Intelligence and Analytics. We typically carry out projects and system implementations for our clients in Singapore and South East Asia region.
You may think: IT, arggg boring folks. No, we're not. We appreciate stylish design.
Attached is our logo that should appear in all slides, larger scale on the title slide and small size in content slides.

Industry/Entity Type

Boutique

```html
<!DOCTYPE html>
<html lang="en">
<head>
<meta charset="utf-8">
<title>Tessalune – Presentation Template</title>
<link rel="stylesheet" href="https://fonts.googleapis.com/css2?family=Arimo:wght@400;700&display=swap">
<style>
  :root {
    --brand-blue: #135392;
    --brand-blue-dark: #0e4a86;
    --title-blue: #0f4f8c;
    --footer-grey: #6e6f71;
    --footer-line: #9a9b9d;
    --logo-grey: #6b6b6d;
    --body-grey: #555557;
    --page-bg: #4b4c4e;
    --white: #ffffff;
    --rule: #9a9a9a;
  }
  * { margin: 0; padding: 0; box-sizing: border-box; }
  html, body { width: 1200px; height: 960px; overflow: hidden; background: var(--page-bg); }
  body { font-family: "Arimo", Arial, sans-serif; }

  .stage {
    width: 1280px; height: 1024px; position: relative;
    transform: scale(0.9375); transform-origin: 0 0;
  }
  .slide {
    position: absolute; width: 563px; height: 422px;
    background: var(--white); overflow: hidden;
    box-shadow: 0 4px 14px rgba(0,0,0,.45);
  }
  .slide--title   { left: 57px;  top: 70px; }
  .slide--chart   { left: 660px; top: 70px; }
  .slide--table   { left: 57px;  top: 532px; }
  .slide--closing { left: 660px; top: 532px; }

  .slide__bg { position: absolute; inset: 0; width: 563px; height: 422px; }

  .slide__footer {
    position: absolute; left: 0; right: 0; bottom: 0; height: 29px;
    background: var(--footer-grey); border-top: 2px solid var(--footer-line);
    color: var(--white); font-size: 13.5px; letter-spacing: .4px;
    display: flex; align-items: center; justify-content: center;
  }
  .slide__footer strong { font-weight: 700; }

  .brand-name {
    position: absolute; left: 0; right: 0; text-align: center;
    color: var(--logo-grey); font-weight: 400; font-size: 70px; letter-spacing: 1px;
  }
  .slide--title .brand-name { top: 102px; }
  .slide--closing .brand-name { top: 100px; }

  .title-block { position: absolute; left: 0; right: 0; top: 272px; text-align: center; color: var(--white); }
  .title-block__title { font-size: 31px; font-weight: 700; letter-spacing: .3px; }
  .title-block__subtitle { font-size: 21px; font-weight: 400; margin-top: 2px; }

  .section-title {
    position: absolute; left: 0; right: 0; top: 24px; text-align: center;
    color: var(--title-blue); font-size: 27px; font-weight: 700;
  }
  .section-rule {
    position: absolute; left: 22px; right: 22px; top: 68px;
    border-top: 1.5px dashed var(--rule);
  }
  .body-copy {
    position: absolute; left: 22px; top: 80px;
    color: var(--body-grey); font-size: 15.5px; line-height: 27.3px;
    text-align: justify;
  }
  .slide--chart .body-copy { width: 364px; }
  .slide--table .body-copy { width: 249px; }

  .chart-illustration {
    position: absolute; left: 398px; top: 84px; width: 160px; height: 256px;
    background: linear-gradient(160deg, #ffffff 0%, #f3c4c4 30%, #3a8fd0 65%, #1566b0 100%);
    border-radius: 4px; opacity: .9;
  }

  .data-table-card {
    position: absolute; left: 284px; top: 68px; width: 261px; height: 168px;
    background: #f3f3f3; padding: 18px 12px 0;
  }
  .data-table-card__caption { font-size: 9.5px; color: #333; text-align: center; margin-bottom: 6px; }
  .data-table { width: 100%; border-collapse: collapse; font-size: 7.5px; color: #222; background: #fff; }
  .data-table th, .data-table td { border: 1px solid #bdbdbd; padding: 3px 3px; text-align: left; height: 16px; }
  .data-table th { font-weight: 700; }
  .data-table td:last-child, .data-table th:last-child { width: 76px; }

  .pie-card { position: absolute; left: 293px; top: 237px; width: 220px; height: 132px; background: #f7f7f7; }

  .thanks {
    position: absolute; left: 45px; top: 278px;
    color: var(--white); font-size: 40px; font-weight: 700;
  }
  .contact {
    position: absolute; right: 23px; top: 249px; text-align: right;
    color: var(--white); font-size: 18px; line-height: 25.5px; font-style: normal;
  }
</style>
</head>
<body>
<main class="stage">

  <section class="slide slide--title" aria-label="Title slide">
    <svg class="slide__bg" viewBox="0 0 563 422" aria-hidden="true">
      <path d="M0 198 Q280 232 563 196 L563 393 L0 393 Z" fill="var(--brand-blue)"/>
      <path d="M0 360 Q200 345 563 350 L563 393 L0 393 Z" fill="var(--brand-blue-dark)" opacity=".5"/>
    </svg>
    <div class="brand-name">Tessalune</div>
    <div class="title-block">
      <h1 class="title-block__title">PRESENTATION TITLE</h1>
      <p class="title-block__subtitle">Subtitle Here</p>
    </div>
    <footer class="slide__footer">Copyright ©&nbsp;www.<strong>tessalune</strong>.sg</footer>
  </section>

  <section class="slide slide--chart" aria-label="Content slide with growth chart">
    <svg class="slide__bg" viewBox="0 0 563 422" aria-hidden="true">
      <path d="M0 366 Q250 348 563 358 L563 393 L0 393 Z" fill="var(--brand-blue)"/>
    </svg>
    <h2 class="section-title">Section Title Here</h2>
    <div class="section-rule"></div>
    <p class="body-copy">Lorem Ipsum este pur şi simplu o machetă pentru text a industriei tipografice. Lorem Ipsum a fost macheta standard a industriei încă din secolul al XVI-lea, când un tipograf anonim a luat o planşetă de litere şi le-a amestecat pentru a crea o carte demonstrativă pentru literele respective. Nu doar că a supravieţuit timp de cinci secole, dar şi a facut saltul în tipografia electronică practic neschimbată. A fost popularizat, ca programele de machetare care includeau versiuni de Lorem Ipsum.</p>
    <div class="chart-illustration" role="img" aria-label="Illustration of rising blue bar chart with red upward arrow"></div>
    <footer class="slide__footer">Copyright ©&nbsp;www.<strong>tessalune</strong>.sg</footer>
  </section>

  <section class="slide slide--table" aria-label="Content slide with table and pie chart">
    <svg class="slide__bg" viewBox="0 0 563 422" aria-hidden="true">
      <path d="M0 366 Q250 348 563 358 L563 393 L0 393 Z" fill="var(--brand-blue)"/>
    </svg>
    <h2 class="section-title">Section Title Here</h2>
    <div class="section-rule"></div>
    <p class="body-copy">Lorem Ipsum este pur şi simplu o machetă pentru text a industriei tipografice. Lorem Ipsum a fost macheta standard a industriei încă din secolul al XVI-lea, când un tipograf anonim a luat o planşetă de litere şi le-a amestecat pentru a crea o carte demonstrativă pentru literele respective. Nu doar că a supravieţuit timp.</p>
    <div class="data-table-card">
      <p class="data-table-card__caption">What animals would you like to see more?</p>
      <table class="data-table">
        <tr><th>Animal</th><th>Requests</th></tr>
        <tr><td>Kittens</td><td>45331</td></tr>
        <tr><td>Puppies</td><td>32323</td></tr>
        <tr><td>Elephants</td><td>12345</td></tr>
        <tr><td>Badgers</td><td>6546</td></tr>
        <tr><td>Sharks (without lasers)</td><td>223</td></tr>
        <tr><td>Sharks (with lasers)</td><td>2323</td></tr>
      </table>
    </div>
    <div class="pie-card"></div>
    <svg class="slide__bg" viewBox="0 0 563 422" role="img" aria-label="Pie chart of animal requests">
      <path d="M412 298 L354.8 280 A60 60 0 0 1 472 300.1 Z" fill="#1bb3bc"/>
      <path d="M412 298 L472 300.1 A60 60 0 0 1 471.1 308.4 Z" fill="#d81b5e"/>
      <path d="M412 298 L471.1 308.4 A60 60 0 0 1 461.7 331.5 Z" fill="#f5a52a"/>
      <path d="M412 298 L461.7 331.5 A60 60 0 0 1 423.4 356.9 Z" fill="#bdf3ec"/>
      <path d="M412 298 L423.4 356.9 A60 60 0 0 1 354.8 280 Z" fill="#8ccde0"/>
    </svg>
    <footer class="slide__footer">Copyright ©&nbsp;www.<strong>tessalune</strong>.sg</footer>
  </section>

  <section class="slide slide--closing" aria-label="Closing slide">
    <svg class="slide__bg" viewBox="0 0 563 422" aria-hidden="true">
      <path d="M0 198 Q280 232 563 196 L563 393 L0 393 Z" fill="var(--brand-blue)"/>
      <path d="M0 360 Q200 345 563 350 L563 393 L0 393 Z" fill="var(--brand-blue-dark)" opacity=".5"/>
    </svg>
    <div class="brand-name">Tessalune</div>
    <p class="thanks">Thank you!</p>
    <address class="contact">
      Your address Goes Here<br>
      City, Country, Zipcode<br>
      p. +00 1234 4567<br>
      f. +00 1234 4567<br>
      office@tessalune.sg
    </address>
    <footer class="slide__footer">Copyright ©&nbsp;www.<strong>tessalune</strong>.sg</footer>
  </section>

</main>
</body>
</html>
```